Business Card Design Project

We're looking for a unique business card design that stands out from the rest, using the brand and logo we've already developed.
Two-sided design please.
Vantor Creative (www.vantorcreative.example.au) is a digitally-focused advertising agency that has produces results-driven campaigns. As a result, we'd like our business card to reflect our innovative approach.
Size, shape, orientation, etc, are all flexible (providing the print costs don't become ridiculous or we have to sit there with tiny scissors!).
Business card should include space for name, title, email, mobile, landline and address.

```html
<!DOCTYPE html>
<html lang="en">
<head>
<meta charset="utf-8">
<title>Vantor Creative – Business Card</title>
<link rel="stylesheet" href="https://fonts.googleapis.com/css2?family=Open+Sans:wght@400;600&display=swap">
<style>
  :root {
    --brand-red: #ed1c24;
    --paper-white: #ffffff;
    --ink-black: #141414;
    --accent-orange: #f7941d;
    --backdrop: #ecebe8;
    --card-radius: 26px;
  }
  html, body {
    margin: 0;
    padding: 0;
    width: 1200px;
    height: 1200px;
    overflow: hidden;
    background: var(--backdrop);
    font-family: "Open Sans", Arial, sans-serif;
  }
  .canvas {
    position: relative;
    width: 1200px;
    height: 1200px;
  }
  .card {
    position: absolute;
    left: 150px;
    width: 900px;
    height: 520px;
    border-radius: var(--card-radius);
    overflow: hidden;
    box-shadow: 0 6px 18px rgba(0, 0, 0, 0.18);
  }
  .card-front { top: 60px; background: var(--brand-red); }
  .card-back { top: 620px; background: var(--paper-white); }
  .card-shapes {
    position: absolute;
    inset: 0;
    width: 100%;
    height: 100%;
  }
  .brand-lockup {
    position: absolute;
    left: 0;
    right: 0;
    top: 175px;
    display: flex;
    align-items: center;
    justify-content: center;
    gap: 22px;
  }
  .brand-dot {
    width: 46px;
    height: 46px;
    border-radius: 50%;
    background: var(--accent-orange);
  }
  .brand-name {
    margin: 0;
    font-weight: 400;
    font-size: 96px;
    line-height: 1;
    letter-spacing: 1px;
    color: var(--ink-black);
  }
  .contact-fields {
    position: absolute;
    inset: 0;
    margin: 0;
    padding: 0;
    list-style: none;
    color: var(--paper-white);
    font-weight: 400;
    font-size: 38px;
    line-height: 1;
  }
  .contact-fields li { position: absolute; }
  .field-name { left: 80px; top: 250px; }
  .field-title { left: 80px; top: 320px; }
  .field-email { left: 80px; top: 390px; }
  .field-mobile { left: 430px; top: 120px; }
  .field-landline { left: 430px; top: 190px; }
  .field-address { left: 430px; top: 260px; }
</style>
</head>
<body>
<main class="canvas">

  <section class="card card-front" aria-label="Card front">
    <svg class="card-shapes" viewBox="0 0 900 520" aria-hidden="true">
      <rect class="front-band" x="0" y="120" width="900" height="270" fill="var(--paper-white)"/>
      <ellipse class="front-swell" cx="470" cy="255" rx="330" ry="190" fill="var(--paper-white)"/>
    </svg>
    <div class="brand-lockup">
      <span class="brand-dot"></span>
      <h1 class="brand-name">Vantor Creative</h1>
    </div>
  </section>

  <section class="card card-back" aria-label="Card back">
    <svg class="card-shapes" viewBox="0 0 900 520" aria-hidden="true">
      <rect class="back-band" x="0" y="170" width="900" height="270" fill="var(--brand-red)"/>
      <ellipse class="back-swell" cx="420" cy="250" rx="330" ry="185" fill="var(--brand-red)"/>
      <path class="back-swoosh" d="M900 330 C 740 330, 560 380, 520 440 L 900 440 Z" fill="var(--paper-white)"/>
      <rect class="back-band-lower" x="0" y="440" width="900" height="80" fill="var(--paper-white)"/>
    </svg>
    <ul class="contact-fields">
      <li class="field-name">Name:</li>
      <li class="field-title">Title:</li>
      <li class="field-email">Email:</li>
      <li class="field-mobile">Mobile:</li>
      <li class="field-landline">Landline:</li>
      <li class="field-address">Address:</li>
    </ul>
  </section>

</main>
</body>
</html>
```